Greeting Card Design Project

We need a greeting card to email our clients during christmas.

We are suppliers for cutting tools & machine accessories. You can find out more about us at our website www.quvantel.com.sg

Reason: I've decide to extend the deadline as I'm awaiting more designs, thank you.

```html
<!DOCTYPE html>
<html lang="en">
<head>
<meta charset="utf-8">
<title>Season's Greetings – Quvantel Tools</title>
<link rel="stylesheet" href="https://fonts.googleapis.com/css2?family=Pinyon+Script&family=Questrial&display=swap">
<style>
  :root {
    --frame-green: #3bab3a;
    --paper: #ffffff;
    --script-green: #2f9a3b;
    --caption-grey: #6d6e70;
    --brand-red: #b0281e;
    --pine-dark: #1f4a26;
    --pine-mid: #3d6b35;
    --pine-light: #7f9b55;
    --berry: #c0251c;
  }
  * { margin: 0; padding: 0; box-sizing: border-box; }
  html, body {
    width: 1200px;
    height: 800px;
    overflow: hidden;
    background: var(--paper);
  }
  .greeting-card {
    position: relative;
    width: 1200px;
    height: 800px;
    border: 16px solid var(--frame-green);
    background: var(--paper);
    overflow: hidden;
  }
  .garland {
    position: absolute;
  }
  .garland--top {
    top: 0; left: 0; right: 0; height: 150px;
    background:
      radial-gradient(ellipse 18% 60% at 22% 20%, rgba(192,37,28,.45), transparent 70%),
      radial-gradient(ellipse 14% 55% at 78% 30%, rgba(192,37,28,.35), transparent 70%),
      linear-gradient(to bottom, var(--pine-dark) 0%, var(--pine-mid) 35%, rgba(127,155,85,.35) 75%, rgba(255,255,255,0) 100%);
  }
  .garland--bottom {
    bottom: 0; left: 0; right: 0; height: 220px;
    background:
      radial-gradient(ellipse 14% 40% at 35% 70%, rgba(192,37,28,.45), transparent 70%),
      radial-gradient(ellipse 12% 40% at 72% 65%, rgba(192,37,28,.4), transparent 70%),
      radial-gradient(ellipse 10% 35% at 88% 40%, rgba(176,110,60,.45), transparent 70%),
      linear-gradient(to top, var(--pine-dark) 0%, var(--pine-mid) 40%, rgba(127,155,85,.35) 80%, rgba(255,255,255,0) 100%);
  }
  .garland--left {
    top: 0; bottom: 0; left: 0; width: 200px;
    background:
      radial-gradient(ellipse 50% 12% at 40% 52%, rgba(192,37,28,.4), transparent 70%),
      linear-gradient(to right, var(--pine-dark) 0%, var(--pine-mid) 35%, rgba(127,155,85,.3) 75%, rgba(255,255,255,0) 100%);
  }
  .garland--right {
    top: 0; bottom: 0; right: 0; width: 200px;
    background:
      radial-gradient(ellipse 50% 12% at 60% 35%, rgba(192,37,28,.4), transparent 70%),
      linear-gradient(to left, var(--pine-dark) 0%, var(--pine-mid) 35%, rgba(127,155,85,.3) 75%, rgba(255,255,255,0) 100%);
  }
  .message {
    position: absolute;
    top: 110px; left: 0; right: 0;
    text-align: center;
  }
  .message__plain {
    font-family: "Questrial", sans-serif;
    font-size: 62px;
    color: var(--caption-grey);
    line-height: 1.1;
  }
  .message__script {
    font-family: "Pinyon Script", cursive;
    font-size: 112px;
    color: var(--script-green);
    line-height: 1.05;
  }
  .brand {
    position: absolute;
    top: 540px; left: 0; right: 0;
    display: flex;
    justify-content: center;
    align-items: center;
    gap: 12px;
  }
  .brand__dot {
    width: 26px; height: 26px;
    border-radius: 50%;
    background: var(--brand-red);
  }
  .brand__name {
    font-family: "Questrial", sans-serif;
    font-size: 30px;
    color: var(--brand-red);
    letter-spacing: 1px;
  }
</style>
</head>
<body>
  <main class="greeting-card">
    <div class="garland garland--top" role="img" aria-label="Pine branches with red baubles and holly berries along the top edge"></div>
    <div class="garland garland--left" role="img" aria-label="Pine branches and red berries along the left edge"></div>
    <div class="garland garland--right" role="img" aria-label="Pine branches, red baubles and berries along the right edge"></div>
    <div class="garland garland--bottom" role="img" aria-label="Pine branches with pine cones, red baubles and holly berries along the bottom edge"></div>

    <section class="message">
      <p class="message__plain">Have A</p>
      <p class="message__script">Merry Christmas</p>
      <p class="message__plain">and a</p>
      <p class="message__script">Happy New Year</p>
    </section>

    <div class="brand">
      <span class="brand__dot"></span>
      <span class="brand__name">QUVANTEL TOOLS</span>
    </div>
  </main>
</body>
</html>
```